Elegant Black Candle Label Design!

I need a 2.375" tall by 3.0" wide candle label design. I'm looking for simple and elegant. Black label with silver leaf border and lettering. Label needs to have the following information on it: Fern Hollow Candle Co. as the company name, scent name in the middle and in smaller font, it needs to say Made in USA, All Natural, 8oz. Attached photos are for inspiration.

Target Market(s)

People looking for high end, all natural candle fragrances

Industry/Entity Type

Candle-Spa

Colors

Designer to choose only greyscale colors for use in the design.

Requirements
Must have
• Company Name, Scent (ability to change scent names), All Natural, Made in USA, 8oz
Nice to have
• Black background, silver leaf border and silver leaf font. Elegant fonts maybe slightly cursive

```html
<!DOCTYPE html>
<html lang="en">
<head>
<meta charset="utf-8">
<title>Fern Hollow Candle Co. – Lavender Sage Label</title>
<link rel="stylesheet" href="https://fonts.googleapis.com/css2?family=Cormorant+Garamond:wght@500&family=Playfair+Display:wght@400&display=swap">
<style>
  :root {
    --label-black: #000000;
    --silver: #b4b4b4;
    --silver-bright: #e8e8e8;
    --silver-soft: rgba(170, 170, 170, 0.28);
  }
  html, body {
    margin: 0;
    padding: 0;
    width: 1200px;
    height: 950px;
    overflow: hidden;
    background: var(--label-black);
  }
  .label {
    position: relative;
    width: 1200px;
    height: 950px;
    background: var(--label-black);
    overflow: hidden;
  }
  .foliage {
    position: absolute;
  }
  .foliage--top-right {
    left: 900px;
    top: 70px;
    width: 300px;
    height: 300px;
    background: radial-gradient(ellipse at 55% 40%, var(--silver-soft) 0%, rgba(170,170,170,0.1) 45%, rgba(0,0,0,0) 72%);
  }
  .foliage--bottom-left {
    left: 0;
    top: 450px;
    width: 470px;
    height: 500px;
    background: radial-gradient(ellipse at 30% 60%, var(--silver-soft) 0%, rgba(170,170,170,0.1) 45%, rgba(0,0,0,0) 72%);
  }
  .frame {
    position: absolute;
    top: 0;
    left: 0;
  }
  .centered {
    position: absolute;
    left: 0;
    width: 1200px;
    text-align: center;
    margin: 0;
    color: var(--silver);
  }
  .brand-name {
    top: 138px;
    font-family: "Playfair Display", serif;
    font-weight: 400;
    font-size: 64px;
    line-height: 1;
    color: var(--silver-bright);
    letter-spacing: 2px;
  }
  .brand-sub {
    top: 222px;
    font-family: "Playfair Display", serif;
    font-weight: 400;
    font-size: 24px;
    line-height: 1;
    color: var(--silver-bright);
    letter-spacing: 12px;
    padding-left: 12px;
  }
  .scent-name {
    top: 348px;
    font-family: "Cormorant Garamond", serif;
    font-weight: 500;
    font-size: 112px;
    line-height: 1;
    letter-spacing: 1px;
  }
  .tagline {
    top: 533px;
    font-family: "Playfair Display", serif;
    font-weight: 400;
    font-size: 35px;
    line-height: 1;
  }
  .claim {
    position: absolute;
    top: 660px;
    width: 240px;
    margin: 0;
    text-align: center;
    font-family: "Playfair Display", serif;
    font-weight: 400;
    font-size: 33px;
    line-height: 39px;
    color: var(--silver);
  }
  .claim--origin { left: 387px; }
  .claim--natural { left: 578px; }
  .net-weight {
    top: 806px;
    font-family: "Playfair Display", serif;
    font-weight: 400;
    font-size: 46px;
    line-height: 1;
  }
</style>
</head>
<body>
<main class="label">
  <div class="foliage foliage--top-right" role="img" aria-label="Silver line-drawn fern frond sweeping over the top right corner"></div>
  <div class="foliage foliage--bottom-left" role="img" aria-label="Silver line-drawn fern fronds rising from the bottom left corner"></div>

  <svg class="frame" width="1200" height="950" viewBox="0 0 1200 950" aria-hidden="true">
    <defs>
      <linearGradient id="silver-sheen" x1="0" y1="0" x2="1" y2="0">
        <stop offset="0" stop-color="#f2f2f2"/>
        <stop offset="0.55" stop-color="#d8d8d8"/>
        <stop offset="0.75" stop-color="#8a8a8a"/>
        <stop offset="1" stop-color="#eeeeee"/>
      </linearGradient>
    </defs>
    <rect x="62.5" y="52.5" width="1071" height="840" fill="none" stroke="url(#silver-sheen)" stroke-width="3.5"/>
    <rect x="73" y="62.5" width="1050" height="820" fill="none" stroke="url(#silver-sheen)" stroke-width="2"/>
    <line class="divider" x1="416" y1="494" x2="784" y2="494" stroke="#b4b4b4" stroke-width="5"/>
    <line class="divider" x1="416" y1="631" x2="784" y2="631" stroke="#b4b4b4" stroke-width="5"/>
    <line class="divider" x1="599.5" y1="631" x2="599.5" y2="764" stroke="#b4b4b4" stroke-width="5"/>
  </svg>

  <p class="centered brand-name">Fern Hollow</p>
  <p class="centered brand-sub">CANDLE CO</p>

  <h1 class="centered scent-name">LAVENDER SAGE</h1>
  <p class="centered tagline">Crafted for balance and relaxation.</p>

  <p class="claim claim--origin">MADE IN<br>USA</p>
  <p class="claim claim--natural">ALL<br>NATURAL</p>

  <p class="centered net-weight">8 OZ</p>
</main>
</body>
</html>
```